Business Card Design

We are looking for a business card designed for our landscaping company. We do landscaping installation & Maintenance Services. We would like to see designs that have basic landscaping in background. We also think it is important to have both of our names and phone numbers on the card. We need something that stands out a little whether it is shape of the card or thickness or design.

Industry/Entity Type

Business

Contact Information for Business Card

Pale Ridge Yardworks, paleridgeyardworks@mailbrook.net, Dale Purvine 555-213-7690, Martin Kolbey 555-864-1037

```html
<!DOCTYPE html>
<html lang="en">
<head>
<meta charset="utf-8">
<title>Pale Ridge Yardworks — Business Card</title>
<link href="https://fonts.googleapis.com/css2?family=Open+Sans:wght@400;600&display=swap" rel="stylesheet">
<style>
  :root {
    --canvas-bg: #e9e7e3;
    --card-white: #f7f7f7;
    --card-shade: #e4e4e4;
    --band-blue: #0a7ccc;
    --band-blue-deep: #0558a6;
    --accent-green: #a9d14a;
    --ink: #141414;
    --band-text: #f2f7fc;
  }
  * { margin: 0; padding: 0; box-sizing: border-box; }
  html, body {
    width: 1200px; height: 892px; overflow: hidden;
    background: var(--canvas-bg);
    font-family: "Open Sans", Arial, sans-serif;
  }
  .stage {
    position: relative; width: 1200px; height: 892px;
    display: flex; align-items: center; justify-content: center;
  }
  .business-card {
    position: relative; width: 840px; height: 480px;
    background: linear-gradient(160deg, #ffffff 0%, var(--card-white) 50%, var(--card-shade) 100%);
    box-shadow: 0 14px 40px rgba(0,0,0,0.18);
    overflow: hidden;
  }
  .card-band { position: absolute; inset: 0; width: 840px; height: 480px; }
  .company-name {
    position: absolute; left: 60px; top: 100px;
    font-size: 46px; font-weight: 400; letter-spacing: 2px;
    color: var(--ink); white-space: nowrap;
  }
  .contact {
    position: absolute; color: var(--band-text);
    font-size: 22px; letter-spacing: 1px; line-height: 1.45;
    white-space: nowrap;
  }
  .contact-phone { display: flex; align-items: center; gap: 10px; font-size: 25px; }
  .phone-icon { width: 18px; height: 18px; flex: none; }
  .contact-primary { left: 300px; top: 352px; }
  .contact-secondary { left: 620px; top: 250px; }
  .contact-email {
    position: absolute; left: 390px; top: 438px;
    color: var(--band-text); font-size: 20px; letter-spacing: 1px;
    white-space: nowrap;
  }
</style>
</head>
<body>
<main class="stage">
  <section class="business-card" aria-label="Pale Ridge Yardworks business card">
    <svg class="card-band" viewBox="0 0 840 480" aria-hidden="true">
      <defs>
        <linearGradient id="bandGradient" x1="0" y1="1" x2="1" y2="0">
          <stop offset="0" stop-color="var(--band-blue)"/>
          <stop offset="1" stop-color="var(--band-blue-deep)"/>
        </linearGradient>
      </defs>
      <path d="M140,480 C220,340 380,300 520,250 C660,200 760,110 840,40 L840,480 Z" fill="url(#bandGradient)"/>
      <path d="M140,480 C220,340 380,300 520,250 C660,200 760,110 840,40" fill="none" stroke="var(--accent-green)" stroke-width="3"/>
    </svg>

    <h1 class="company-name">Pale Ridge Yardworks</h1>

    <div class="contact contact-secondary">
      <p class="contact-name">Martin Kolbey</p>
      <p class="contact-phone">
        <svg class="phone-icon" viewBox="0 0 18 18" aria-hidden="true"><rect width="18" height="18" rx="3" fill="#ffffff"/><path d="M5 4 L7 4 L8 7 L6.5 8 C7.3 9.8 8.3 10.8 10 11.5 L11 10 L14 11 L14 13 C9 14 4 9 5 4 Z" fill="var(--band-blue)"/></svg>
        555-864-1037
      </p>
    </div>

    <div class="contact contact-primary">
      <p class="contact-name">Dale Purvine</p>
      <p class="contact-phone">
        <svg class="phone-icon" viewBox="0 0 18 18" aria-hidden="true"><rect width="18" height="18" rx="3" fill="#ffffff"/><path d="M5 4 L7 4 L8 7 L6.5 8 C7.3 9.8 8.3 10.8 10 11.5 L11 10 L14 11 L14 13 C9 14 4 9 5 4 Z" fill="var(--band-blue)"/></svg>
        555-213-7690
      </p>
    </div>

    <p class="contact-email">paleridgeyardworks@mailbrook.net</p>
  </section>
</main>
</body>
</html>
```